Product Packaging Redesign

We have an existing package layout that needs to be redesigned to include our product name, Brisk Tunebox, our UPC and more appealing/professional designs.

Changes will include artwork, images, SKU, product details and description etc.

Product campaign can be viewed here http://brisktunebox-demo.net

You can get details, images etc from there.

Looking for retail friendly design, appealing to buyers.
Updates

Industry/Entity Type

Retail

Colors

Designer to choose colors to be used in the design.

Requirements
Must have
• Package renamed to Brisk Tunebox
UPC changed to ours (see attached file)
Clean, appealing retail design
Nice to have
• Logo for Brisk Tunebox created/added to package

```html
<!DOCTYPE html>
<html lang="en">
<head>
<meta charset="utf-8">
<title>Brisk Tunebox Packaging Project</title>
<link rel="stylesheet" href="https://fonts.googleapis.com/css2?family=Inter:wght@300;400;700&display=swap">
<style>
  :root {
    --paper: #ffffff;
    --ink: #111111;
    --grey: #8a8a8a;
    --edge: #e2e2e2;
    --red: #e0143f;
    --orange: #e8951a;
    --gold: #d8c415;
    --blue: #6aa5e6;
    --speaker-dark: #1e2628;
    --speaker-mid: #3d484b;
    --speaker-ring: #3c8fd0;
  }
  * { box-sizing: border-box; margin: 0; padding: 0; }
  html, body { width: 1200px; height: 795px; overflow: hidden; background: var(--paper); }
  body { font-family: "Inter", Arial, sans-serif; color: var(--ink); position: relative; }

  .dieline-row {
    position: absolute; left: 85px; top: 80px;
    display: flex; gap: 20px; align-items: flex-end;
  }
  .box { display: flex; flex-direction: column; width: 190px; }
  .red { --accent: var(--red); }
  .orange { --accent: var(--orange); }
  .gold { --accent: var(--gold); }
  .blue { --accent: var(--blue); }

  /* top panel */
  .top-panel {
    height: 140px; background: var(--paper); border: 1px solid var(--edge);
    border-bottom: none; position: relative;
  }
  .top-panel .brand-name {
    position: absolute; left: 12px; top: 14px;
    font-size: 11px; font-weight: 700; letter-spacing: -0.2px;
  }
  .top-panel .product-photo {
    position: absolute; left: 50%; top: 42px; width: 100px; height: 44px;
    transform: translateX(-50%); border-radius: 6px;
    background: radial-gradient(ellipse at 50% 45%, var(--speaker-mid), var(--speaker-dark) 75%);
  }
  .top-icons {
    position: absolute; left: 50%; top: 100px; transform: translateX(-50%);
    display: flex; gap: 5px;
  }
  .top-icons span {
    width: 18px; height: 13px; border-radius: 2px; background: var(--accent);
  }

  /* front and side panels */
  .panel {
    height: 260px; background: var(--paper);
    border: 1px solid var(--edge); position: relative; overflow: hidden;
  }
  .panel .band {
    position: absolute; left: 0; right: 0; top: 78px; height: 130px;
    background: var(--accent);
  }
  .panel .brand-name {
    position: absolute; left: 0; right: 0; top: 48px;
    text-align: center; font-size: 19px; font-weight: 700; letter-spacing: -0.4px;
  }
  .panel .product-photo {
    position: absolute; left: 50%; top: 90px; width: 104px; height: 108px;
    transform: translateX(-50%); border-radius: 8px;
    background: radial-gradient(ellipse at 50% 35%, var(--speaker-mid), var(--speaker-dark) 72%);
  }
  .tagline {
    position: absolute; left: 0; right: 0; bottom: 18px;
    text-align: center; color: var(--grey); line-height: 1.05;
  }
  .tagline .small { font-size: 7px; letter-spacing: 0.5px; }
  .tagline .large { font-size: 11px; letter-spacing: 0.6px; font-weight: 300; }

  .side-panel .brand-name { text-align: left; left: 12px; font-size: 15px; top: 54px; }
  .spec { position: absolute; left: 12px; right: 10px; top: 88px; color: var(--paper); }
  .spec h3 { font-size: 8px; font-weight: 700; margin-bottom: 2px; }
  .spec h3.accessory { margin-top: 6px; }
  .spec p { font-size: 6px; line-height: 1.35; }
  .feature-icons { position: absolute; left: 10px; bottom: 14px; display: flex; gap: 6px; }
  .feature-icon {
    width: 30px; height: 30px; background: var(--red); border-radius: 4px;
    display: flex; align-items: center; justify-content: center;
  }

  .project-title { position: absolute; left: 849px; top: 543px; line-height: 1.1; }
  .project-title .name { font-size: 31px; font-weight: 700; letter-spacing: -0.6px; }
  .project-title .label { font-size: 25px; letter-spacing: -0.5px; }
  .project-title .label b { font-weight: 700; }
  .project-title .colours { font-size: 22px; letter-spacing: -0.4px; margin-top: 4px; }
  .project-title .colours b { font-weight: 700; }
</style>
</head>
<body>
  <main class="dieline-row">
    <div class="box red">
      <section class="panel side-panel">
        <div class="band"></div>
        <div class="brand-name">Brisk Tunebox</div>
        <div class="spec">
          <h3>specification</h3>
          <p>Splashproof portable speaker<br>Built-in microphone<br>Suction cup mount<br>Hands-free calling<br>Clear stereo output<br>Charges via USB cable</p>
          <h3 class="accessory">accessory</h3>
          <p>USB charging cable<br>User manual</p>
        </div>
        <div class="feature-icons">
          <span class="feature-icon"><svg width="16" height="16" viewBox="0 0 16 16"><rect x="3" y="3" width="10" height="10" fill="none" stroke="#fff" stroke-width="1.6"/></svg></span>
          <span class="feature-icon"><svg width="16" height="16" viewBox="0 0 16 16" fill="none" stroke="#fff" stroke-width="1.6"><path d="M2 7a9 9 0 0 1 12 0M4.5 9.5a5 5 0 0 1 7 0"/><circle cx="8" cy="12" r="1" fill="#fff"/></svg></span>
          <span class="feature-icon"><svg width="16" height="16" viewBox="0 0 16 16" fill="none" stroke="#fff" stroke-width="1.6"><path d="M3 10V8a5 5 0 0 1 10 0v2"/><rect x="2" y="9" width="3" height="4"/><rect x="11" y="9" width="3" height="4"/></svg></span>
          <span class="feature-icon"><svg width="16" height="16" viewBox="0 0 16 16" fill="none" stroke="#fff" stroke-width="1.6"><rect x="1.5" y="4.5" width="11" height="7"/><path d="M14 7v2"/><path d="M4 6.5v3M6.5 6.5v3M9 6.5v3"/></svg></span>
        </div>
      </section>
    </div>

    <div class="box red">
      <section class="top-panel">
        <div class="brand-name">Brisk Tunebox</div>
        <div class="product-photo" role="img" aria-label="Top view photo of the dark round speaker"></div>
        <div class="top-icons"><span></span><span></span><span></span><span></span></div>
      </section>
      <section class="panel">
        <div class="band"></div>
        <div class="brand-name">Brisk Tunebox</div>
        <div class="product-photo" role="img" aria-label="Product photo of the dark round suction-cup speaker with blue ring"></div>
        <div class="tagline"><div class="small">WIRELESS MUSIC</div><div class="large">BLUETOOTH</div></div>
      </section>
    </div>

    <div class="box orange">
      <section class="top-panel">
        <div class="brand-name">Brisk Tunebox</div>
        <div class="product-photo" role="img" aria-label="Top view photo of the dark round speaker"></div>
        <div class="top-icons"><span></span><span></span><span></span><span></span></div>
      </section>
      <section class="panel">
        <div class="band"></div>
        <div class="brand-name">Brisk Tunebox</div>
        <div class="product-photo" role="img" aria-label="Product photo of the dark round suction-cup speaker with blue ring"></div>
        <div class="tagline"><div class="small">WIRELESS MUSIC</div><div class="large">BLUETOOTH</div></div>
      </section>
    </div>

    <div class="box gold">
      <section class="top-panel">
        <div class="brand-name">Brisk Tunebox</div>
        <div class="product-photo" role="img" aria-label="Top view photo of the dark round speaker"></div>
        <div class="top-icons"><span></span><span></span><span></span><span></span></div>
      </section>
      <section class="panel">
        <div class="band"></div>
        <div class="brand-name">Brisk Tunebox</div>
        <div class="product-photo" role="img" aria-label="Product photo of the dark round suction-cup speaker with blue ring"></div>
        <div class="tagline"><div class="small">WIRELESS MUSIC</div><div class="large">BLUETOOTH</div></div>
      </section>
    </div>

    <div class="box blue">
      <section class="top-panel">
        <div class="brand-name">Brisk Tunebox</div>
        <div class="product-photo" role="img" aria-label="Top view photo of the dark round speaker"></div>
        <div class="top-icons"><span></span><span></span><span></span><span></span></div>
      </section>
      <section class="panel">
        <div class="band"></div>
        <div class="brand-name">Brisk Tunebox</div>
        <div class="product-photo" role="img" aria-label="Product photo of the dark round suction-cup speaker with blue ring"></div>
        <div class="tagline"><div class="small">WIRELESS MUSIC</div><div class="large">BLUETOOTH</div></div>
      </section>
    </div>
  </main>

  <aside class="project-title">
    <div class="name">Brisk Tunebox</div>
    <div class="label"><b>Packaging</b>project</div>
    <div class="colours"><b>red</b>orange<b>gold</b>blue</div>
  </aside>
</body>
</html>
```